Become a Mentor - For Musicians, Artists, Producers and Teachers

Here is the full creative brief:

https://files.plenwick.com/sheets/d/4kTqpLm8Wz_2RNa7Hc3Xv91Jd0Gb5YeUsQ6fNo8rTpxa/view?mode=shared

Here is the background image file: https://www.trovecrate.com/sh/83jbwtrmq5dkx2u/BBHn4k7QTf2ZpLeXX-wr9MUHe?dl=0

LOGO:
https://www.trovecrate.com/sh/k472rufmpdo9b6w/BBKLe3RtHY5J-sFQnLZw7Ggma?dl=0

```html
<!DOCTYPE html>
<html lang="en">
<head>
<meta charset="utf-8">
<title>Become a Mentor Today – Campaign Set</title>
<link href="https://fonts.googleapis.com/css2?family=Montserrat:wght@500;600;700;800&display=swap" rel="stylesheet">
<style>
  :root {
    --page: #ffffff;
    --white: #ffffff;
    --ink: #111111;
    --black: #050508;
    --cyan: #8fe9f2;
    --photo-light: #8c8f96;
    --photo-mid: #4a4c52;
    --photo-dark: #1d1e22;
    --galaxy-deep: #131a3d;
    --galaxy-blue: #2c5b8c;
    --galaxy-violet: #5a3f78;
    --galaxy-rose: #7a3f5e;
  }
  * { box-sizing: border-box; margin: 0; padding: 0; }
  html, body { width: 1200px; height: 900px; overflow: hidden; background: var(--page); }
  body { position: relative; font-family: "Montserrat", Arial, sans-serif; color: var(--white); }

  .artboard { position: absolute; overflow: hidden; background: var(--black); }
  .artboard--poster { left: 13px; top: 10px; width: 620px; height: 877px; }
  .artboard--cover { left: 655px; top: 10px; width: 530px; height: 233px; }
  .artboard--post { left: 655px; top: 281px; width: 485px; height: 606px; }

  .photo {
    position: absolute; inset: 0;
    background:
      radial-gradient(ellipse at 30% 55%, rgba(230,225,215,0.55), transparent 45%),
      radial-gradient(ellipse at 75% 40%, rgba(60,40,35,0.6), transparent 40%),
      linear-gradient(160deg, var(--photo-light) 0%, var(--photo-mid) 45%, var(--photo-dark) 100%);
  }
  .galaxy {
    position: absolute; inset: 0;
    background:
      radial-gradient(ellipse at 20% 80%, rgba(122,63,94,0.75), transparent 55%),
      radial-gradient(ellipse at 80% 30%, rgba(44,91,140,0.85), transparent 60%),
      linear-gradient(120deg, var(--galaxy-deep), var(--galaxy-blue) 45%, var(--galaxy-violet) 80%, var(--galaxy-rose));
  }
  .base { position: absolute; inset: 0; background: var(--black); }

  .stripes { position: absolute; }

  .kicker { position: absolute; font-weight: 800; text-transform: uppercase; letter-spacing: -0.5px; }
  .headline { position: absolute; font-weight: 600; letter-spacing: -2px; white-space: nowrap; }
  .tagline { position: absolute; color: var(--cyan); font-weight: 600; }
  .audience { position: absolute; font-weight: 500; }
  .contact { position: absolute; font-weight: 600; }
  .contact .cta { color: var(--cyan); font-weight: 700; }

  .brand { position: absolute; display: flex; align-items: center; gap: 8px; }
  .brand__dot { border-radius: 50%; background: var(--white); flex: none; }
  .brand__name { font-weight: 700; text-transform: uppercase; line-height: 1.05; color: var(--white); }

  .label { position: absolute; font-size: 9.5px; font-weight: 800; text-transform: uppercase; color: var(--ink); }
  .label--poster { color: var(--white); }
</style>
</head>
<body>

<!-- A4 poster -->
<section class="artboard artboard--poster">
  <div class="photo" role="img" aria-label="Two young men talking in a music studio beside a mixing desk and speaker"></div>
  <div class="galaxy" style="clip-path: polygon(0 385px, 620px 420px, 620px 877px, 0 877px);"></div>
  <div class="base" style="clip-path: polygon(0 770px, 620px 680px, 620px 877px, 0 877px);"></div>
  <svg class="stripes" style="left:527px; top:0;" width="80" height="80" viewBox="0 0 80 80">
    <g stroke="#fff" stroke-width="4">
      <line x1="0" y1="20" x2="20" y2="0"/><line x1="0" y1="40" x2="40" y2="0"/>
      <line x1="0" y1="60" x2="60" y2="0"/><line x1="0" y1="80" x2="80" y2="0"/>
      <line x1="20" y1="80" x2="80" y2="20"/><line x1="40" y1="80" x2="80" y2="40"/>
      <line x1="60" y1="80" x2="80" y2="60"/>
    </g>
  </svg>
  <p class="kicker" style="left:42px; top:44px; font-size:27px; line-height:26px;">Start<br>Your<br>Career</p>
  <h1 class="headline" style="left:40px; top:405px; font-size:82px; line-height:84px;">Become a<br>Mentor Today</h1>
  <p class="tagline" style="left:43px; top:568px; font-size:28px; line-height:26px;">Turn your skills and passion for<br>music into a career</p>
  <p class="audience" style="left:43px; top:640px; font-size:22px; line-height:30px;">Designed for<br>Musicians, Artists<br>Producers &amp; Teachers</p>
  <p class="contact" style="left:43px; top:777px; font-size:17px; line-height:23px;"><span class="cta">APPLY NOW</span><br>Call 1300 482 482<br>www.meridianschoolofmusic.com.au</p>
  <div class="brand" style="left:430px; top:795px;">
    <span class="brand__dot" style="width:14px; height:14px;"></span>
    <span class="brand__name" style="font-size:15px;">Meridian<br>School of Music</span>
  </div>
  <span class="label label--poster" style="left:552px; top:862px;">A4 Poster</span>
</section>

<!-- Facebook cover -->
<section class="artboard artboard--cover">
  <div class="photo" role="img" aria-label="Two young men talking in a music studio"></div>
  <div class="galaxy" style="clip-path: polygon(235px 0, 530px 0, 530px 233px, 150px 233px);"></div>
  <div class="base" style="clip-path: polygon(0 190px, 530px 155px, 530px 233px, 0 233px);"></div>
  <svg class="stripes" style="left:15px; top:0;" width="58" height="40" viewBox="0 0 58 40">
    <g stroke="#fff" stroke-width="3">
      <line x1="0" y1="15" x2="15" y2="0"/><line x1="0" y1="30" x2="30" y2="0"/>
      <line x1="5" y1="40" x2="45" y2="0"/><line x1="20" y1="40" x2="58" y2="2"/>
      <line x1="35" y1="40" x2="58" y2="17"/>
    </g>
  </svg>
  <p class="kicker" style="right:20px; top:18px; font-size:20px; line-height:18px; text-align:right;">Start<br>Your<br>Career</p>
  <h2 class="headline" style="right:18px; top:72px; font-size:50px; line-height:48px; text-align:right; letter-spacing:-1.5px;">Become a<br>Mentor Today</h2>
  <p class="contact" style="left:18px; top:196px; font-size:17px; font-weight:700;">www.meridianschoolofmusic.com.au</p>
  <div class="brand" style="right:14px; top:193px;">
    <span class="brand__dot" style="width:10px; height:10px;"></span>
    <span class="brand__name" style="font-size:10px;">Meridian<br>School of Music</span>
  </div>
</section>
<span class="label" style="left:655px; top:249px;">Facebook Cover</span>
<span class="label" style="left:655px; top:267px;">Instagram Post</span>

<!-- Instagram post -->
<section class="artboard artboard--post">
  <div class="photo" role="img" aria-label="Two young men talking in a music studio beside a mixing desk and speaker"></div>
  <div class="galaxy" style="clip-path: polygon(0 330px, 485px 355px, 485px 606px, 0 606px);"></div>
  <div class="base" style="clip-path: polygon(0 500px, 485px 440px, 485px 606px, 0 606px);"></div>
  <svg class="stripes" style="left:383px; top:0;" width="80" height="80" viewBox="0 0 80 80">
    <g stroke="#fff" stroke-width="3.5">
      <line x1="0" y1="20" x2="20" y2="0"/><line x1="0" y1="40" x2="40" y2="0"/>
      <line x1="0" y1="60" x2="60" y2="0"/><line x1="0" y1="80" x2="80" y2="0"/>
      <line x1="20" y1="80" x2="80" y2="20"/><line x1="40" y1="80" x2="80" y2="40"/>
      <line x1="60" y1="80" x2="80" y2="60"/>
    </g>
  </svg>
  <p class="kicker" style="left:23px; top:17px; font-size:23px; line-height:22px;">Start<br>Your<br>Career</p>
  <h2 class="headline" style="left:21px; top:324px; font-size:62px; line-height:62px; letter-spacing:-1.5px;">Become a<br>Mentor Today</h2>
  <p class="tagline" style="left:24px; top:453px; font-size:21px; line-height:19px;">Turn your skills and passion for<br>music into a career</p>
  <p class="contact" style="left:22px; top:535px; font-size:13.5px; line-height:18px;"><span class="cta">APPLY NOW</span><br>Call 1300 482 482<br>www.meridianschoolofmusic.com.au</p>
  <div class="brand" style="left:318px; top:538px;">
    <span class="brand__dot" style="width:12px; height:12px;"></span>
    <span class="brand__name" style="font-size:12.5px;">Meridian<br>School of Music</span>
  </div>
</section>

</body>
</html>
```